Breezeway Comfort business cards design

Need a business card design for a Heating and Air Conditioning business. I need these items included.
Business name: Breezeway Comfort
Owner: Marcus Tollefsen
License # 2874590
Phone number # 555-382-4071
Email: breezewaycomfortair@mailvista.example
Sales
Service
Installation
Maintenance

Heating and Air Conditioning

Requirements
Must have
• Company name , license number , phone number , email

```html
<!DOCTYPE html>
<html lang="en">
<head>
<meta charset="utf-8">
<title>Breezeway Comfort – Business Cards</title>
<link href="https://fonts.googleapis.com/css2?family=Arimo:wght@400;700&display=swap" rel="stylesheet">
<style>
  :root {
    --navy: #1c3f9c;
    --orange: #ee7a2a;
    --orange-light: #f29a2e;
    --red: #df4a3c;
    --paper: #ffffff;
    --backdrop: #e9e9eb;
  }
  * { box-sizing: border-box; margin: 0; padding: 0; }
  html, body { width: 1200px; height: 900px; overflow: hidden; }
  body {
    background: var(--backdrop);
    font-family: "Arimo", Arial, sans-serif;
    position: relative;
  }
  .card {
    position: absolute;
    left: 250px;
    width: 700px;
    height: 400px;
    background: var(--paper);
    border-radius: 24px;
    overflow: hidden;
    box-shadow: 0 8px 24px rgba(0,0,0,0.18);
  }
  .card-front { top: 35px; }
  .card-back { top: 465px; }

  .front-name {
    position: absolute;
    left: 0; right: 0; top: 170px;
    text-align: center;
    font-weight: 700;
    font-size: 50px;
    color: var(--navy);
    letter-spacing: 1px;
    text-transform: uppercase;
  }

  .back-name {
    position: absolute;
    left: 40px; top: 60px;
    font-weight: 700;
    font-size: 34px;
    color: var(--navy);
    text-transform: uppercase;
    letter-spacing: 0.5px;
  }
  .services {
    position: absolute;
    right: 40px; top: 26px;
    list-style: none;
    color: var(--orange);
    font-weight: 700;
    font-size: 16px;
    line-height: 20px;
    text-transform: uppercase;
  }
  .services li::before { content: "• "; }

  .owner-block {
    position: absolute;
    left: 40px; top: 165px;
  }
  .owner-name {
    font-weight: 700;
    font-size: 30px;
    color: var(--navy);
    text-transform: uppercase;
  }
  .owner-role {
    font-weight: 700;
    font-size: 24px;
    color: var(--orange);
    line-height: 28px;
  }
  .owner-license {
    font-weight: 700;
    font-size: 15px;
    color: var(--navy);
    margin-top: 2px;
  }

  .wave { position: absolute; inset: 0; width: 700px; height: 400px; }

  .contact {
    position: absolute;
    left: 40px; bottom: 22px;
    color: var(--paper);
    font-weight: 700;
  }
  .contact-phone { font-size: 36px; line-height: 42px; }
  .contact-email { font-size: 27px; line-height: 32px; }
</style>
</head>
<body>

<section class="card card-front">
  <div class="front-name">Breezeway Comfort</div>
</section>

<section class="card card-back">
  <svg class="wave" viewBox="0 0 700 400" aria-hidden="true">
    <defs>
      <linearGradient id="bandFill" x1="0" y1="0" x2="0.3" y2="1">
        <stop offset="0" stop-color="#f29a2e"/>
        <stop offset="0.6" stop-color="#ec6f2c"/>
        <stop offset="1" stop-color="#df4a3c"/>
      </linearGradient>
    </defs>
    <path d="M0,282 C220,280 420,180 700,140 L700,400 L0,400 Z" fill="url(#bandFill)"/>
    <path d="M0,272 C220,270 420,168 700,128" fill="none" stroke="#1c3f9c" stroke-width="6"/>
  </svg>

  <div class="back-name">Breezeway Comfort</div>

  <ul class="services">
    <li>Sales</li>
    <li>Service</li>
    <li>Installation</li>
    <li>Maintenance</li>
  </ul>

  <div class="owner-block">
    <div class="owner-name">Marcus Tollefsen</div>
    <div class="owner-role">owner</div>
    <div class="owner-license">License # 2874590</div>
  </div>

  <div class="contact">
    <div class="contact-phone">555-382-4071</div>
    <div class="contact-email">breezewaycomfortair@mailvista.example</div>
  </div>
</section>

</body>
</html>
```